KTW Structural Approval Partners Certifiers

Professional Construction Consultancy Company Business Card - must keep logo colours see images below - examples have been added from my last competition - please see them as examples only!

Target Market(s)

Home Builders

Industry/Entity Type

Construction

Contact Information for Business Card

See "must haves"

Font styles to use
Sans Serif

Colors
ffffff
add136
000000

Requirements
Must have
• Daniel Moravec
• Director
• Phone: 0431 758 219
• Address: 17 Corrigan St,
• Holloway Vale, SA, 5098
• Email: ktwapprovalpartners@mailbox-example.com
• Website: www.ktwapprovalpartners.example.au
• Facebook: KTW Structural Approval Partners
Nice to have
• Side 1: full logo
• Side 2: company details
Should not have
• hard to read
• must be clear and professional

```html
<!DOCTYPE html>
<html lang="en">
<head>
<meta charset="utf-8">
<title>KTW Structural Approval Partners – Business Card</title>
<link rel="stylesheet" href="https://fonts.googleapis.com/css2?family=Montserrat:wght@700&family=Lato:wght@400;700&display=swap">
<style>
  :root {
    --green: #add136;
    --black: #000000;
    --white: #ffffff;
    --stage: #222222;
  }
  * { box-sizing: border-box; margin: 0; padding: 0; }
  html, body { width: 1189px; height: 1200px; overflow: hidden; background: var(--stage); }
  .card {
    position: absolute; left: 171px; width: 856px; height: 488px;
    background: var(--white); overflow: hidden;
  }
  .card--front { top: 67px; }
  .card--back { top: 626px; }

  .brand { display: flex; align-items: center; gap: 16px; font-family: "Montserrat", sans-serif; font-weight: 700; color: var(--black); white-space: nowrap; }
  .brand__mark { width: 58px; height: 58px; background: var(--green); flex: none; }
  .brand__name { line-height: 1.15; }
  .brand__line { display: block; font-size: 31px; text-transform: uppercase; }
  .brand__tag { display: block; font-size: 24px; letter-spacing: 0.55em; text-transform: uppercase; margin-top: 6px; }

  .card--front .brand { position: absolute; left: 50%; top: 50%; transform: translate(-50%, -50%); }

  .card--back .brand { position: absolute; left: 43px; top: 80px; }
  .card--back .brand__line { font-size: 25px; }
  .card--back .brand__tag { font-size: 20px; }
  .card--back .brand__mark { width: 48px; height: 48px; }

  .accent-panel {
    position: absolute; top: 0; right: 0; width: 250px; height: 488px;
    background: linear-gradient(to right, rgba(173, 209, 54, 0) 0%, var(--green) 45%);
  }

  .person { position: absolute; left: 40px; top: 250px; display: flex; align-items: center; font-family: "Lato", sans-serif; white-space: nowrap; }
  .person__name { font-weight: 700; font-size: 30px; color: var(--black); padding-right: 10px; border-right: 2px solid var(--black); line-height: 1.25; }
  .person__role { font-size: 25px; color: var(--green); padding-left: 10px; }

  .contacts { position: absolute; left: 40px; top: 314px; list-style: none; font-family: "Lato", sans-serif; font-size: 22px; color: var(--black); white-space: nowrap; }
  .contacts li { display: flex; align-items: center; gap: 8px; height: 28.7px; }
  .contacts svg { width: 24px; height: 24px; flex: none; }
  .icon-bg { fill: var(--green); }
  .icon-fg { fill: none; stroke: var(--white); stroke-width: 1.8; stroke-linecap: round; stroke-linejoin: round; }
  .icon-fill { fill: var(--white); }
</style>
</head>
<body>

<section class="card card--front" aria-label="Card front">
  <div class="brand">
    <span class="brand__mark"></span>
    <span class="brand__name">
      <span class="brand__line">KTW Structural</span>
      <span class="brand__line">Approval Partners</span>
      <span class="brand__tag">Certifiers</span>
    </span>
  </div>
</section>

<section class="card card--back" aria-label="Card back">
  <div class="accent-panel" role="img" aria-label="Green decorative accent area"></div>

  <div class="brand">
    <span class="brand__mark"></span>
    <span class="brand__name">
      <span class="brand__line">KTW Structural</span>
      <span class="brand__line">Approval Partners</span>
      <span class="brand__tag">Certifiers</span>
    </span>
  </div>

  <div class="person">
    <span class="person__name">DANIEL MORAVEC</span>
    <span class="person__role">Director</span>
  </div>

  <ul class="contacts">
    <li>
      <svg viewBox="0 0 24 24" aria-hidden="true"><rect class="icon-bg" width="24" height="24"/><path class="icon-fg" d="M7 6 L10 6 L11 9 L9.5 10.5 C10.5 12.5 11.5 13.5 13.5 14.5 L15 13 L18 14 L18 17 C12 18 6 12 7 6 Z"/></svg>
      <span>0431 758 219</span>
    </li>
    <li>
      <svg viewBox="0 0 24 24" aria-hidden="true"><rect class="icon-bg" width="24" height="24"/><rect class="icon-fg" x="5" y="7" width="14" height="10"/><path class="icon-fg" d="M5 7 L12 13 L19 7"/></svg>
      <span>ktwapprovalpartners@mailbox-example.com</span>
    </li>
    <li>
      <svg viewBox="0 0 24 24" aria-hidden="true"><rect class="icon-bg" width="24" height="24"/><circle class="icon-fg" cx="12" cy="12" r="7"/><path class="icon-fg" d="M5 12 H19 M12 5 C9 9 9 15 12 19 M12 5 C15 9 15 15 12 19"/></svg>
      <span>www.ktwapprovalpartners.example.au</span>
    </li>
    <li>
      <svg viewBox="0 0 24 24" aria-hidden="true"><rect class="icon-bg" width="24" height="24"/></svg>
      <span>KTW Structural Approval Partners</span>
    </li>
    <li>
      <svg viewBox="0 0 24 24" aria-hidden="true"><rect class="icon-bg" width="24" height="24"/><path class="icon-fill" d="M12 4 C8.7 4 6.5 6.4 6.5 9.3 C6.5 13 12 20 12 20 C12 20 17.5 13 17.5 9.3 C17.5 6.4 15.3 4 12 4 Z"/><circle cx="12" cy="9.3" r="2.2" fill="#add136"/></svg>
      <span>17 Corrigan St, Holloway Vale, SA, 5098</span>
    </li>
  </ul>
</section>

</body>
</html>
```